New Body Mist 250 ml exclusive

We are excited to embark on a new project to design the packaging for body mist:
Dewy Marigold

We are looking for a design that is truly unique and stands out, with a touch of individuality that sets it apart. The design should be eye-catching and visually appealing, drawing attention even from a distance. We want the body mists to have a fun and attractive look that appeals to customers.

To help bring your design to life, we will provide the dimensions of the bottle, which has a capacity of 250ml. The bottle measures 13.3 cm in height and 4.9 cm in diameter (excluding the pump). Additionally, we will also provide the dimensions of the label, which measures 15.1 cm in height and 12.8 cm in width.

We believe that giving you the freedom to put your own unique touch and color choices will help create a truly standout design. We look forward to seeing your creative vision for our body mist.

We shared with you the logo of the body mist and some examples of models that we liked.

Please be informed that the project only includes one design and the remaining three will be completed and paid for through a 1on1 project with the winner of the contest.

Target Market(s)

Supermarket and perfumery stores

Industry/Entity Type

Cosmetics

Font styles to use
Serif

Requirements
Must have
• Uniqueness and attractiveness

```html
<!DOCTYPE html>
<html lang="en">
<head>
<meta charset="utf-8">
<title>Dewy Marigold Body Mist Labels</title>
<link rel="stylesheet" href="https://fonts.googleapis.com/css2?family=Josefin+Sans:wght@600&family=Playfair+Display:wght@400;500&family=Oswald:wght@300&display=swap">
<style>
  :root {
    --bg: #e9ded4;
    --white: #ffffff;
    --lilac-top: #b872b8;
    --lilac-mid: #e6d8ee;
    --sky-top: #4a89c2;
    --sky-mid: #cfe6f4;
    --sunset-top: #e8804a;
    --sunset-mid: #f6c9ae;
    --meadow: #4fae6a;
    --meadow-deep: #1e9a4c;
    --lime: #a5bf3a;
    --plum: #a2239a;
    --indigo: #3a2d9a;
    --crimson: #cf1d2c;
    --volume: rgba(255,255,255,0.85);
  }
  * { margin: 0; padding: 0; box-sizing: border-box; }
  html, body { width: 836px; height: 1200px; overflow: hidden; }
  body {
    background: var(--bg);
    display: flex;
    justify-content: center;
    align-items: center;
    gap: 36px;
  }
  .label {
    position: relative;
    width: 226px;
    height: 660px;
    border-radius: 6px;
    overflow: hidden;
  }
  .label--rain { background: linear-gradient(180deg, var(--lilac-top) 0%, #c9a0cf 25%, var(--lilac-mid) 42%, #bfe0ef 55%, #8fcfc4 70%, var(--meadow) 100%); }
  .label--orchid { background: linear-gradient(180deg, var(--sky-top) 0%, #86b6de 25%, var(--sky-mid) 45%, #9ad8d8 62%, #4fb98a 80%, var(--meadow-deep) 100%); }
  .label--sunset { background: linear-gradient(180deg, var(--sunset-top) 0%, #ec9f7b 25%, var(--sunset-mid) 40%, #e5d5a8 58%, #c8d07a 78%, var(--lime) 100%); }
  .brand {
    position: absolute;
    top: 54px;
    width: 100%;
    text-align: center;
    font-family: "Josefin Sans", sans-serif;
    font-weight: 600;
    font-size: 17px;
    letter-spacing: 0.14em;
    text-transform: uppercase;
    color: var(--white);
  }
  .scent {
    position: absolute;
    top: 130px;
    width: 100%;
    text-align: center;
    font-family: "Playfair Display", serif;
    font-weight: 400;
    text-transform: uppercase;
    line-height: 0.95;
  }
  .scent__main { display: block; font-size: 46px; letter-spacing: -0.02em; }
  .scent__sub { display: block; font-size: 32px; letter-spacing: -0.02em; }
  .label--rain .scent { color: var(--plum); }
  .label--orchid .scent { color: var(--indigo); }
  .label--sunset .scent { color: var(--crimson); }
  .flowers {
    position: absolute;
    left: 0;
    top: 250px;
    width: 100%;
    height: 340px;
  }
  .label--rain .flowers { background: radial-gradient(ellipse 45% 25% at 55% 22%, rgba(176,110,200,0.5), transparent), radial-gradient(ellipse 50% 25% at 50% 72%, rgba(110,150,120,0.35), transparent); }
  .label--orchid .flowers { background: radial-gradient(ellipse 40% 22% at 60% 20%, rgba(226,100,160,0.45), transparent), radial-gradient(ellipse 50% 25% at 50% 75%, rgba(60,140,90,0.35), transparent); }
  .label--sunset .flowers { background: radial-gradient(ellipse 35% 22% at 58% 18%, rgba(230,110,170,0.45), transparent), radial-gradient(ellipse 50% 25% at 40% 68%, rgba(240,210,90,0.4), transparent); }
  .volume {
    position: absolute;
    left: 18px;
    bottom: 26px;
    font-family: "Oswald", sans-serif;
    font-weight: 300;
    font-size: 20px;
    color: var(--volume);
  }
</style>
</head>
<body>
  <section class="label label--rain">
    <p class="brand">Dewy Marigold</p>
    <h2 class="scent"><span class="scent__main">Rain</span><span class="scent__sub">Whisper</span></h2>
    <div class="flowers" role="img" aria-label="Photo of lilac cosmos flowers over a misty green meadow"></div>
    <p class="volume">250ml</p>
  </section>
  <section class="label label--orchid">
    <p class="brand">Dewy Marigold</p>
    <h2 class="scent"><span class="scent__main">Meadow</span><span class="scent__sub">Orchid</span></h2>
    <div class="flowers" role="img" aria-label="Photo of pink cosmos flowers on tall stems against a blue sky and green field"></div>
    <p class="volume">250ml</p>
  </section>
  <section class="label label--sunset">
    <p class="brand">Dewy Marigold</p>
    <h2 class="scent"><span class="scent__main">Sunset</span><span class="scent__sub">Forever</span></h2>
    <div class="flowers" role="img" aria-label="Photo of a pink cosmos flower against a warm sunset over yellow wildflowers"></div>
    <p class="volume">250ml</p>
  </section>
</body>
</html>
```